Property Management business needs Business cards designed

We provide a premium property management service based in Sydney's Norther Beaches. We want people to feel confident in choosing us to manage their investment properties. We offer a much more personalized service than other estate agents.
We want a modern clean design. Something that shows confidence without being complicated.
Logo attached.

Target Market(s)

35-70yo Male and Female with strong property portfolios within Sydney's Norther Beaches

Industry/Entity Type

Property Management

Contact Information for Business Card

Address: Suite 7, 12-14 Kelvin Parade, Harlow NSW 2188
Two separate named cards.
Tom Ardley - 0491 570 118 tom@harbourvaleestates.com.au
Clara Dunmore - 0491 570 263 clara@harbourvaleestates.com.au

Requirements
Must have
• Business logo, name, number, address, email.

```html
<!DOCTYPE html>
<html lang="en">
<head>
<meta charset="utf-8">
<title>Harbourvale Estates – Business Card</title>
<link rel="stylesheet" href="https://fonts.googleapis.com/css2?family=Roboto:wght@400;500;700&display=swap">
<style>
  :root {
    --page-bg: #ffffff;
    --card-white: #ffffff;
    --teal-light: #12808a;
    --teal-deep: #0b5f69;
    --sand: #d8d2bb;
    --icon-teal: #3aa3ab;
    --text-light: #ffffff;
    --text-dark: #1a1a1a;
  }
  * { box-sizing: border-box; margin: 0; padding: 0; }
  html, body {
    width: 1200px;
    height: 1200px;
    overflow: hidden;
    background: var(--page-bg);
    font-family: "Roboto", Arial, sans-serif;
  }
  .business-card {
    position: absolute;
    left: 150px;
    top: 324px;
    width: 900px;
    height: 552px;
    background: var(--card-white);
    overflow: hidden;
    box-shadow: 0 0 0 1px #ececec;
  }
  .card-shapes {
    position: absolute;
    inset: 0;
    width: 100%;
    height: 100%;
  }
  .brand-name {
    position: absolute;
    right: 44px;
    top: 128px;
    font-size: 31px;
    font-weight: 700;
    letter-spacing: 0.5px;
    color: var(--text-dark);
    white-space: nowrap;
  }
  .contact-block {
    position: absolute;
    left: 54px;
    top: 190px;
    color: var(--text-light);
  }
  .person-name {
    font-size: 32px;
    font-weight: 700;
    margin-bottom: 30px;
  }
  .contact-line {
    display: flex;
    align-items: flex-start;
    font-size: 23px;
    font-weight: 400;
    line-height: 31px;
    margin-bottom: 20px;
  }
  .contact-icon {
    flex: 0 0 24px;
    width: 24px;
    height: 24px;
    margin-right: 14px;
    margin-top: 3px;
    fill: var(--icon-teal);
  }
</style>
</head>
<body>
  <div class="business-card">
    <svg class="card-shapes" viewBox="0 0 900 552" preserveAspectRatio="none">
      <defs>
        <linearGradient id="tealFill" x1="0" y1="0" x2="1" y2="1">
          <stop offset="0" stop-color="var(--teal-light)"/>
          <stop offset="1" stop-color="var(--teal-deep)"/>
        </linearGradient>
      </defs>
      <polygon class="sand-band" points="148,0 178,0 900,540 900,552 872,552" fill="var(--sand)"/>
      <polygon class="teal-panel" role="img" aria-label="Teal faceted geometric background panel"
               points="0,0 148,0 872,552 0,552" fill="url(#tealFill)"/>
    </svg>

    <div class="brand-name">HARBOURVALE ESTATES</div>

    <div class="contact-block">
      <p class="person-name">Tom Ardley</p>
      <p class="contact-line">
        <svg class="contact-icon" viewBox="0 0 24 24" aria-hidden="true">
          <path d="M7 1h10a2 2 0 0 1 2 2v18a2 2 0 0 1-2 2H7a2 2 0 0 1-2-2V3a2 2 0 0 1 2-2zm1 3v8h8V4H8zm1 10v2h2v-2H9zm4 0v2h2v-2h-2zm-4 3v2h2v-2H9zm4 0v2h2v-2h-2z"/>
        </svg>
        <span>0491 570 118</span>
      </p>
      <p class="contact-line">
        <svg class="contact-icon" viewBox="0 0 24 24" aria-hidden="true">
          <path d="M1 5h22v2l-11 7L1 7V5zm0 4.4l11 7 11-7V19H1V9.4z"/>
        </svg>
        <span>tom@harbourvaleestates.com.au</span>
      </p>
      <p class="contact-line">
        <svg class="contact-icon" viewBox="0 0 24 24" aria-hidden="true">
          <path d="M3 2l19 10L3 22z"/>
        </svg>
        <span>Suite 7, 12-14 Kelvin Parade,<br>Harlow NSW 2188</span>
      </p>
    </div>
  </div>
</body>
</html>
```